card design for engineering consultancy

engineering drafting and project management company the provides drafting services for.
Electrical, Hydraulic, Mechanical, and Civil services
The company is called Q7R Services and logo is as attached
Information on card should be.
1. Logo
2.website : Q7RServices.example
3. email : info@Q7RServices.example
4. Phone: (+61) 400512836
5. Motto: Design - Document - Develop - Deliver

this card should be basically used for business identification only

Target Market(s)

electricians plumbers air conditioning installers and civil contractors

Industry/Entity Type

engineering, drafting, electrical, plumbing, airconditioning, civil

Contact Information for Business Card

1. Logo 2.website : Q7RServices.example 3. email : info@Q7RServices.example 4. Phone: (+61) 400512836 5. Motto: Design - Document - Develop - Deliver

Font styles to use
Serif

Requirements
Must have
• logo
Nice to have
• something inovative and different that makes it stand out from being just another business card

```html
<!DOCTYPE html>
<html lang="en">
<head>
<meta charset="utf-8">
<title>Q7R Services — Business Card</title>
<link rel="stylesheet" href="https://fonts.googleapis.com/css2?family=Archivo:wght@800&family=Tinos&display=swap">
<style>
  :root {
    --backdrop-light: #e2e2e2;
    --backdrop-dark: #c8c8c8;
    --card-black: #0c0c0c;
    --card-black-soft: #2a2a2a;
    --card-white: #ffffff;
    --ink-grey: #454545;
    --silver: #c4c4c4;
    --brand-red: #d3202f;
    --band-grey: #4a4a4a;
    --rule-grey: #9a9a9a;
    --text-dark: #2b2b2b;
  }
  * { margin: 0; padding: 0; box-sizing: border-box; }
  html, body { width: 1200px; height: 852px; overflow: hidden; }
  body {
    background: radial-gradient(ellipse at 50% 40%, var(--backdrop-light), var(--backdrop-dark));
    position: relative;
  }
  .card {
    position: absolute;
    top: 272px;
    width: 540px;
    height: 309px;
    border-radius: 18px;
    overflow: hidden;
    box-shadow: 0 6px 18px rgba(0,0,0,0.25);
  }
  .card-front {
    left: 40px;
    background: linear-gradient(135deg, var(--card-black-soft) 0%, var(--card-black) 55%);
    display: flex;
    align-items: center;
    justify-content: center;
  }
  .card-back { left: 620px; background: var(--card-white); }

  .brand {
    display: flex;
    align-items: center;
    gap: 12px;
    font-family: "Archivo", Arial, sans-serif;
    font-weight: 800;
    text-transform: uppercase;
    letter-spacing: 2px;
    white-space: nowrap;
  }
  .brand-mark { width: 16px; height: 16px; flex: none; }
  .card-front .brand { color: var(--silver); font-size: 34px; }
  .card-front .brand-mark { background: var(--silver); width: 20px; height: 20px; }
  .card-back .brand {
    position: absolute;
    left: 34px;
    top: 126px;
    color: var(--ink-grey);
    font-size: 24px;
  }
  .card-back .brand-mark { background: var(--brand-red); }

  .divider {
    position: absolute;
    left: 300px;
    top: 58px;
    width: 1px;
    height: 96px;
    background: var(--rule-grey);
  }
  .contact-list {
    position: absolute;
    left: 322px;
    top: 64px;
    list-style: none;
    font-family: "Tinos", "Times New Roman", serif;
    font-size: 15px;
    color: var(--text-dark);
  }
  .contact-list li {
    display: flex;
    align-items: center;
    gap: 8px;
    height: 24px;
    white-space: nowrap;
  }
  .contact-list svg { width: 13px; height: 13px; flex: none; }

  .bands { position: absolute; left: 0; bottom: 0; width: 540px; height: 74px; }
  .motto {
    position: absolute;
    right: 18px;
    top: 244px;
    font-family: "Archivo", Arial, sans-serif;
    font-weight: 800;
    font-size: 12px;
    letter-spacing: 1px;
    color: #fff;
    text-transform: uppercase;
    line-height: 12px;
    white-space: nowrap;
  }
  .motto .dot { color: var(--brand-red); margin: 0 3px; }
</style>
</head>
<body>
  <section class="card card-front" aria-label="Card front">
    <div class="brand"><span class="brand-mark"></span>Q7R Services</div>
  </section>

  <section class="card card-back" aria-label="Card back">
    <div class="brand"><span class="brand-mark"></span>Q7R Services</div>
    <div class="divider"></div>
    <ul class="contact-list">
      <li>
        <svg viewBox="0 0 16 16" aria-hidden="true"><circle cx="8" cy="8" r="8" fill="var(--brand-red)"/><path d="M5 4.5c.6-.5 1.2-.4 1.5.2l.6 1.2c.2.4 0 .8-.3 1l-.4.3c.4.9 1.1 1.6 2 2l.3-.4c.3-.3.7-.4 1-.2l1.2.6c.6.3.7.9.2 1.5-.6.7-1.5.9-2.4.5C6.8 10.5 5.5 9.2 4.8 7.3c-.4-1 0-2.1.2-2.8z" fill="#fff"/></svg>
        (+61) 400512836
      </li>
      <li>
        <svg viewBox="0 0 16 16" aria-hidden="true"><rect x="1" y="3" width="14" height="10" rx="1" fill="var(--brand-red)"/><path d="M1.5 3.5 8 9l6.5-5.5" fill="none" stroke="#fff" stroke-width="1.2"/></svg>
        info@Q7RServices.example
      </li>
      <li>
        <svg viewBox="0 0 16 16" aria-hidden="true"><circle cx="8" cy="8" r="7.5" fill="var(--brand-red)"/><ellipse cx="8" cy="8" rx="3" ry="7" fill="none" stroke="#fff" stroke-width="1"/><path d="M1 8h14" stroke="#fff" stroke-width="1"/></svg>
        Q7RServices.example
      </li>
    </ul>

    <svg class="bands" viewBox="0 0 540 74" aria-hidden="true">
      <polygon points="186,0 540,0 540,30 170,30" fill="var(--band-grey)"/>
      <polygon points="0,38 190,38 170,74 0,74" fill="var(--brand-red)"/>
    </svg>
    <p class="motto">Design<span class="dot">•</span>Document<span class="dot">•</span>Develop<span class="dot">•</span>Deliver</p>
  </section>
</body>
</html>
```